4x6 Postcard Design Full Color Double Sided

Hello, I am in need of a postcard design. The document with details is attached. And I am writing here also:

To My Dear Colleague,

This week, I want you to do yourself and me a favor, okay?

I want you to ask your boss for a $100,000 per year salary increase. If the answer is no then I want you to “give yourself” a

$10,000 per month pay increase RIGHT NOW!

The opportunity to make 6-7 figures using SIMPLE online systems is exploding right before your eyes. Why aren’t you paying attention? Is It because you don’t have any idea how to earn money online? Or are you intimidated by the thought of it because you’re not tech-savvy?

Throw any negative thoughts out of your mind and let us help you build a $100,000 + yearly income that runs on automatic. We’re not promising a million dollars overnight or that you’ll be able to quit your job tomorrow, BUT if an extra $10,000 per month would help you reach your goals, then you should take action today!

OUR SIMPLE IS SO EASY TO USE, A FIFTH GRADER COULD BE SUCCESSFUL!

We’re so sure you will be successful with our system that we are inviting you to
GET STARTED TODAY FOR FREE!!!

That’s right…for FREE! No credit card is required.

GO SIGN UP NOW:
www.qmvhub.com/joinFREE
Enter Referral ID#

LK-R7859

Free offer expires in 48 hours!!!

Instructions for designers:
I’d like the color scheme to stay consistent with my company’s color scheme. To see the color scheme of Blue Harbor Gain go to www.qmvhub.com
As you are reading the text, please make certain parts of the text be emphasized on the postcard – wherever you feel necessary. When you read it, what would catch your attention? Those parts are the parts I’d like you to emphasize on the card by making them bolder, or a different color, or larger or highlighted.

The postcard is a 4x6 card, double-sided, full color

The text above is for the front side. The back will be the same thing, except in the spot where I have LK-R7859. On the backside it should say: (Use ID# on reverse side)

It’s like you are really only designing a one-sided card because the back side is almost an exact duplicate.

Thank you, you rock! =)

Target Market(s)

work from home seekers / make money online enthusiasts

Font styles to use
Serif

Requirements
Must have
• Color scheme similar to the color scheme at www.qmvhub.com
• The rest of the requirements are attached to the word doc.
• I will also send the logo, but it wouldn't let me upload because the file is too large.
Nice to have
• I really I am looking for something that really looks clean, but attention-grabbing

```html
<!DOCTYPE html>
<html lang="en">
<head>
<meta charset="utf-8">
<title>Blue Harbor Gain – Postcard</title>
<link rel="stylesheet" href="https://fonts.googleapis.com/css2?family=Montserrat:wght@500;600&family=Raleway:wght@400;500&display=swap">
<style>
  :root {
    --ink: #1f1f1f;
    --brand-blue: #7cc9e0;
    --sky-top: #ffffff;
    --sky-mid: #e9f1f6;
    --sky-low: #c9dbe7;
    --ridge: #a9c1d3;
    --badge-fill: #ffffff;
  }
  * { margin: 0; padding: 0; box-sizing: border-box; }
  html, body { width: 800px; height: 1200px; overflow: hidden; }
  body {
    font-family: "Raleway", Arial, sans-serif;
    color: var(--ink);
    background: var(--sky-top);
  }
  .postcard {
    position: relative;
    width: 800px;
    height: 1200px;
    overflow: hidden;
  }
  .sky-scene {
    position: absolute;
    inset: 0;
    background: linear-gradient(180deg, var(--sky-top) 0%, var(--sky-top) 22%, var(--sky-mid) 45%, var(--sky-low) 72%, var(--ridge) 100%);
  }
  .greeting {
    position: absolute;
    left: 48px;
    top: 90px;
    font-family: "Montserrat", Arial, sans-serif;
    font-weight: 500;
    font-size: 23px;
    line-height: 28px;
  }
  .brand-name {
    position: absolute;
    left: 404px;
    top: 88px;
    font-family: "Montserrat", Arial, sans-serif;
    font-weight: 500;
    font-size: 32px;
    line-height: 36px;
    color: var(--ink);
  }
  .copy {
    position: absolute;
    left: 54px;
    width: 706px;
    font-size: 20px;
    line-height: 29px;
  }
  .callout {
    position: absolute;
    left: 54px;
    width: 712px;
    font-family: "Montserrat", Arial, sans-serif;
    font-weight: 500;
    font-size: 23px;
    line-height: 29px;
  }
  .callout--caps { text-transform: uppercase; letter-spacing: 1px; }
  .p-favor { top: 212px; }
  .p-boss { top: 271px; }
  .c-raise { top: 356px; }
  .p-opportunity { top: 414px; }
  .p-negative { top: 558px; }
  .c-simple { top: 726px; }
  .p-inviting { top: 813px; width: 680px; }
  .c-start { top: 900px; }
  .p-free { top: 955px; width: 380px; }
  .c-signup { top: 1046px; }
  .referral-badge {
    position: absolute;
    left: 496px;
    top: 842px;
    width: 260px;
    height: 260px;
    border-radius: 50%;
    border: 7px solid var(--brand-blue);
    background: var(--badge-fill);
    display: flex;
    flex-direction: column;
    align-items: center;
    justify-content: center;
    text-align: center;
    font-family: "Montserrat", Arial, sans-serif;
    font-weight: 500;
  }
  .referral-label { font-size: 17px; line-height: 24px; }
  .referral-id { font-size: 28px; margin: 14px 0 12px; letter-spacing: 0.5px; }
  .referral-expiry { font-size: 17px; line-height: 25px; }
</style>
</head>
<body>
  <main class="postcard">
    <div class="sky-scene" role="img" aria-label="Soft misty blue mountain range fading up into a pale sky"></div>

    <p class="greeting">To My Dear Colleague,</p>

    <p class="brand-name">Blue Harbor Gain</p>

    <p class="copy p-favor">This week, I want you to do yourself and me a favor, okay?</p>

    <p class="copy p-boss">I want you to ask your boss for a $100,000 per year salary increase. If the answer is no then I want you to “give yourself” a</p>

    <p class="callout c-raise">$10,000 per month pay increase RIGHT NOW!</p>

    <p class="copy p-opportunity">The opportunity to make 6-7 figures using SIMPLE online systems is exploding right before your eyes. Why aren’t you paying attention? Is It because you don’t have any idea how to earn money online?&nbsp; Or are you intimidated by the thought of it because you’re not tech-savvy?</p>

    <p class="copy p-negative">Throw any negative thoughts out of your mind and let us help you build a $100,000 + yearly income that runs on automatic. We’re not promising a million dollars overnight or that you’ll be able to quit your job tomorrow, BUT if an extra $10,000 per month would help you reach your goals, then you should take action today!</p>

    <p class="callout callout--caps c-simple">Our simple is so easy to use, a fifth grader<br>could be successful!</p>

    <p class="copy p-inviting">We’re so sure you will be successful with our system that we are<br>inviting you to</p>

    <p class="callout callout--caps c-start">Get started today for free!!!</p>

    <p class="copy p-free">That’s right…for FREE!<br>No credit card is required.</p>

    <p class="callout c-signup">GO SIGN UP NOW:<br>www.qmvhub.com/joinFREE</p>

    <div class="referral-badge">
      <p class="referral-label">Enter<br>Referral ID#</p>
      <p class="referral-id">LK-R7859</p>
      <p class="referral-expiry">Free offer expires<br>in 48 hours!!!</p>
    </div>
  </main>
</body>
</html>
```